Professional and creatice Life Coach - Business Card design

I just relaunched my website and now i a need a correspoonding business card for my task as life coach. My website is www.tbalrond.com as reference. The compass is kind of a symbol for my work, as I help people navigate through their challenging phases in life. The business card should be colorful, but not too playful as I also adress business people. So it sould be creative, but professional (also to suport my other business as Management Consultant)

Target Market(s)

People who want to get teir problems resolved, in business, partnership and other personal realms

Industry/Entity Type

Life Coaching

Contact Information for Business Card

Front side should include Name, Phone number, Email, Website and address

Font styles to use
Sans Serif

Colors
add136

Requirements
Must have
• "Mag. Leopold Brantner" -> Name
"Energetische Praxis" -> Jobtitle (describing my profession as life coach)
colours and style should match my website www.tbalrond.com
Nice to have
• a compass as a symbol

```html
<!DOCTYPE html>
<html lang="de">
<head>
<meta charset="utf-8">
<title>Leopold Brantner – Visitenkarte</title>
<link rel="stylesheet" href="https://fonts.googleapis.com/css2?family=Mulish:wght@400;500&display=swap">
<style>
  :root {
    --backdrop: #8f8f8f;
    --card: #231f20;
    --green: #4cb748;
    --white: #ffffff;
    --deco: #3a3637;
  }
  html, body {
    margin: 0;
    padding: 0;
    width: 1200px;
    height: 960px;
    overflow: hidden;
    background: var(--backdrop);
    font-family: "Mulish", sans-serif;
  }
  .canvas {
    position: relative;
    width: 1200px;
    height: 960px;
  }
  .card {
    position: absolute;
    left: 281px;
    width: 655px;
    height: 373px;
    background: var(--card);
    border-radius: 22px;
    overflow: hidden;
  }
  .card--front { top: 59px; }
  .card--back  { top: 501px; }

  .brand-name {
    position: absolute;
    left: 76px;
    top: 86px;
    margin: 0;
    font-size: 28px;
    font-weight: 500;
    letter-spacing: 0.3px;
    color: var(--green);
  }
  .person-name {
    position: absolute;
    left: 76px;
    top: 147px;
    margin: 0;
    font-size: 24px;
    font-weight: 500;
    color: var(--green);
  }
  .job-title {
    position: absolute;
    left: 76px;
    top: 176px;
    margin: 0;
    font-size: 17px;
    font-weight: 400;
    color: var(--white);
  }
  .contact-list {
    position: absolute;
    left: 76px;
    top: 218px;
    margin: 0;
    padding: 0;
    list-style: none;
  }
  .contact-list li {
    display: flex;
    align-items: center;
    height: 24px;
    font-size: 16px;
    color: var(--white);
  }
  .contact-list svg {
    width: 14px;
    height: 14px;
    margin-right: 7px;
    flex: none;
  }

  .compass-area {
    position: absolute;
    top: 66px;
    width: 240px;
    height: 240px;
    border-radius: 50%;
    background: radial-gradient(circle, #4a4647 0%, var(--deco) 70%);
  }
  .card--front .compass-area { right: -120px; }
  .card--back  .compass-area { left: -120px; }

  .back-url {
    position: absolute;
    left: 219px;
    top: 176px;
    margin: 0;
    font-size: 14px;
    letter-spacing: 2px;
    color: var(--white);
  }
  .back-mark {
    position: absolute;
    left: 431px;
    top: 140px;
    width: 160px;
    display: flex;
    flex-direction: column;
    align-items: center;
  }
  .back-mark__dot {
    width: 44px;
    height: 44px;
    border-radius: 50%;
    background: var(--green);
  }
  .back-mark__name {
    margin-top: 12px;
    font-size: 14px;
    font-weight: 500;
    letter-spacing: 1px;
    color: var(--green);
    white-space: nowrap;
  }
</style>
</head>
<body>
<main class="canvas">

  <section class="card card--front">
    <h1 class="brand-name">LEOPOLD BRANTNER</h1>
    <h2 class="person-name">Mag. Leopold Brantner</h2>
    <p class="job-title">Energetische Praxis</p>
    <ul class="contact-list">
      <li>
        <svg viewBox="0 0 16 16" aria-hidden="true"><path fill="#4cb748" d="M3.2 1.5l2.6 2.4-1.4 2c1 2 2.6 3.6 4.6 4.6l2-1.4 2.4 2.6-1.6 2C7 13.5 2.5 9 1.5 3.1z"/></svg>
        123 123 1234
      </li>
      <li>
        <svg viewBox="0 0 16 16" aria-hidden="true"><rect x="1" y="3.5" width="14" height="9" fill="#4cb748"/><path d="M1 3.5l7 5 7-5" fill="none" stroke="#231f20" stroke-width="1.2"/></svg>
        info@tbalrond.com
      </li>
      <li>
        <svg viewBox="0 0 16 16" aria-hidden="true"><g fill="none" stroke="#4cb748" stroke-width="1.3"><circle cx="8" cy="8" r="6.5"/><ellipse cx="8" cy="8" rx="3" ry="6.5"/><path d="M1.5 8h13M2.6 4.8h10.8M2.6 11.2h10.8"/></g></svg>
        www.tbalrond.com
      </li>
    </ul>
    <div class="compass-area" role="img" aria-label="Compass decoration at the card edge"></div>
  </section>

  <section class="card card--back">
    <div class="compass-area" role="img" aria-label="Compass decoration at the card edge"></div>
    <p class="back-url">www.tbalrond.com</p>
    <div class="back-mark">
      <span class="back-mark__dot"></span>
      <span class="back-mark__name">LEOPOLD BRANTNER</span>
    </div>
  </section>

</main>
</body>
</html>
```